Mina Vell makeup artist business cards

Hello
I need business cards for my freelance makeup artist business.

What I am looking for;
Sleek
Clear and easily read
Expensive/exclusive feel
Black and white
Embossed

Information that must be included on back
My name
My contact number
My email
My website
My Facebook
My Instagram

If it works I'd like to also include on the back;
Bridal, glamour, evening, editorial, fashion, tv, film makeup
(Open to exclude if it makes the card look to busy)

Requirements
Must have
• My logo mina Vell makeup artist as shown in photos
Nice to have
• I'd like to see some designs with the social media icons (as shown in image attached)

```html
<!DOCTYPE html>
<html lang="en">
<head>
<meta charset="utf-8">
<title>Mina Vell — Makeup Artist Business Cards</title>
<link rel="stylesheet" href="https://fonts.googleapis.com/css2?family=Josefin+Sans:wght@300;400&display=swap">
<style>
  :root {
    --backdrop: #d9d9d9;
    --card-black: #0b0b0b;
    --ink-light: #ececec;
    --ink-soft: #bdbdbd;
    --mark-fill: #dcdcdc;
  }
  * { margin: 0; padding: 0; box-sizing: border-box; }
  html, body {
    width: 1200px;
    height: 1200px;
    overflow: hidden;
    background: var(--backdrop);
  }
  .sheet {
    width: 1200px;
    height: 1200px;
    display: flex;
    flex-direction: column;
    align-items: center;
    justify-content: center;
    gap: 60px;
    font-family: "Josefin Sans", sans-serif;
    font-weight: 300;
    color: var(--ink-light);
  }
  .card {
    width: 840px;
    height: 480px;
    background: var(--card-black);
    box-shadow: 0 10px 30px rgba(0,0,0,0.18);
    position: relative;
  }

  /* Front */
  .card--front {
    display: flex;
    flex-direction: column;
    align-items: center;
    justify-content: center;
  }
  .brand-mark {
    width: 110px;
    height: 110px;
    border-radius: 50%;
    background: var(--mark-fill);
    margin-bottom: 36px;
  }
  .brand-name {
    font-size: 40px;
    letter-spacing: 0.38em;
    margin-right: -0.38em;
    text-transform: uppercase;
    line-height: 1;
  }
  .brand-role {
    margin-top: 12px;
    font-size: 17px;
    letter-spacing: 0.5em;
    margin-right: -0.5em;
    text-transform: uppercase;
    color: var(--ink-soft);
  }

  /* Back */
  .card--back {
    display: flex;
    align-items: center;
  }
  .back-brand {
    width: 340px;
    display: flex;
    flex-direction: column;
    align-items: center;
    gap: 22px;
  }
  .back-brand .brand-mark {
    width: 150px;
    height: 150px;
    margin: 0;
  }
  .back-brand .brand-name {
    font-size: 18px;
    letter-spacing: 0.4em;
    margin-right: -0.4em;
  }
  .divider {
    width: 1px;
    height: 300px;
    background: var(--ink-light);
    opacity: 0.8;
  }
  .contact-list {
    list-style: none;
    margin-left: 56px;
    display: flex;
    flex-direction: column;
    gap: 14px;
  }
  .contact-item {
    display: flex;
    align-items: center;
    gap: 18px;
    font-size: 18px;
    letter-spacing: 0.3em;
    text-transform: uppercase;
    line-height: 1;
  }
  .contact-icon {
    width: 20px;
    height: 20px;
    flex: none;
  }
</style>
</head>
<body>
  <main class="sheet">
    <section class="card card--front" aria-label="Business card front">
      <div class="brand-mark" aria-hidden="true"></div>
      <h1 class="brand-name">Mina Vell</h1>
      <p class="brand-role">Makeup Artist</p>
    </section>

    <section class="card card--back" aria-label="Business card back">
      <div class="back-brand">
        <div class="brand-mark" aria-hidden="true"></div>
        <p class="brand-name">Mina Vell</p>
      </div>
      <div class="divider" aria-hidden="true"></div>
      <ul class="contact-list">
        <li class="contact-item">
          <svg class="contact-icon" viewBox="0 0 20 20" aria-hidden="true">
            <circle cx="10" cy="10" r="9" fill="none" stroke="var(--ink-light)" stroke-width="1.4"/>
            <path d="M7 5.5 L8.6 5.5 L9.3 8 L8.2 8.9 Q9 11 11.1 11.8 L12 10.7 L14.5 11.4 L14.5 13 Q14.5 14 13.4 14 Q6 13.6 6 6.6 Q6 5.5 7 5.5 Z" fill="var(--ink-light)"/>
          </svg>
          <span>999-99-99</span>
        </li>
        <li class="contact-item">
          <svg class="contact-icon" viewBox="0 0 20 20" aria-hidden="true"><circle cx="10" cy="10" r="9" fill="none" stroke="var(--ink-light)" stroke-width="1.4"/></svg>
          <span>yourwebsite.com</span>
        </li>
        <li class="contact-item">
          <svg class="contact-icon" viewBox="0 0 20 20" aria-hidden="true">
            <circle cx="10" cy="10" r="9" fill="none" stroke="var(--ink-light)" stroke-width="1.4"/>
            <rect x="5.5" y="7" width="9" height="6.5" fill="none" stroke="var(--ink-light)" stroke-width="1.2"/>
            <path d="M5.5 7 L10 10.6 L14.5 7" fill="none" stroke="var(--ink-light)" stroke-width="1.2"/>
          </svg>
          <span>emailaddress@com</span>
        </li>
        <li class="contact-item">
          <svg class="contact-icon" viewBox="0 0 20 20" aria-hidden="true"><circle cx="10" cy="10" r="9" fill="none" stroke="var(--ink-light)" stroke-width="1.4"/></svg>
          <span>yourpage.com</span>
        </li>
        <li class="contact-item">
          <svg class="contact-icon" viewBox="0 0 20 20" aria-hidden="true"><circle cx="10" cy="10" r="9" fill="none" stroke="var(--ink-light)" stroke-width="1.4"/></svg>
          <span>yourgallery.com</span>
        </li>
      </ul>
    </section>
  </main>
</body>
</html>
```